website design for Brixa Motor Gleam llc. an automotive Dry Ice detailling and cleaning business.

We need a website designed for an automotive detailing/cleaning company. I would like a grayscale style with the chosen colors to accent/highlight. We use super dry, compressed air to propel precisely processed, uniform particles of dry ice to clean and/or remove dirt and contaminants form vehicles concentrating mainly on undercarriage, engine bay and wheels/wheel wells. This process prevents water/moisture getting into areas of the vehicle you don't want it.

Target Market(s)

vehicle owners with luxury and/or collector cars

Industry/Entity Type

automotive dry ice detailing and cleaning

Coding

Coded - Design and coding required

Number of Pages Required

2 page

Font styles to use
Sans Serif

Colors
0054AA
0677BA
7BADD7
CADEEF
E8F1F8
00AB8E
00BBA5
67D7C9
C6EFE9
E9F9F6
EB3D1F
EC4F4E
F09395
F8D3D4
FCEDEE

Requirements
Must have
• logo prominently displayed on a darker background area. Links to social media and other businesses I am associated with. Photos and short video, sync with social so last (how many?3,5?) posts automatically sync with/show up on website.
Nice to have
• mostly grayscale with chosen colors to accentuate or for attention, excitement

```html
<!DOCTYPE html>
<html lang="en">
<head>
<meta charset="utf-8">
<title>Brixa Motor Gleam llc — Dry Ice Cleaning</title>
<link rel="stylesheet" href="https://fonts.googleapis.com/css2?family=Fira+Sans:wght@400;500;600;700&family=Roboto:wght@400;500;700&display=swap">
<style>
:root{
  --red:#e41e26;
  --sky:#5bc8e6;
  --sky-deep:#3fb4d8;
  --navy:#0b2a40;
  --navy-dark:#07202f;
  --ink:#1d1d1d;
  --muted:#3a3a3a;
  --gray-band:#ececec;
  --white:#ffffff;
  --footer:#15181b;
}
*{margin:0;padding:0;box-sizing:border-box}
html,body{width:1200px;height:3470px;overflow:hidden}
body{position:relative;background:var(--white);font-family:"Fira Sans",sans-serif;color:var(--ink)}
.shapes{position:absolute;left:0;top:0}
/* header */
.brand{position:absolute;display:flex;align-items:center;gap:10px;font-family:"Fira Sans",sans-serif;font-weight:700;color:var(--red);white-space:nowrap}
.brand-dot{width:20px;height:20px;border-radius:50%;background:var(--sky)}
.brand.top{left:89px;top:46px;font-size:23px}
.nav{position:absolute;top:36px;left:540px;display:flex;gap:33px;font-family:"Roboto",sans-serif;font-weight:500;font-size:15px;color:var(--white)}
.nav .active{color:var(--red);text-decoration:underline}
.btn-book{position:absolute;left:995px;top:28px;width:117px;height:35px;background:var(--red);color:var(--white);font-family:"Roboto",sans-serif;font-weight:500;font-size:15px;display:flex;align-items:center;justify-content:center}
.hero-title{position:absolute;left:0;width:1233px;top:224px;text-align:center;font-weight:700;font-size:60px;letter-spacing:1px;color:var(--sky)}
.hero-sub{position:absolute;left:0;width:1233px;top:290px;text-align:center;font-size:21px;color:var(--white)}
.dots{position:absolute;top:449px;left:574px;display:flex;gap:9px}
.dots span{width:12px;height:12px;border-radius:50%;border:1.5px solid var(--white)}
.dots .on{background:var(--red);border-color:var(--red)}
/* about */
.h2{position:absolute;font-weight:500;font-size:41px;color:var(--red)}
.about-text{position:absolute;left:89px;top:705px;width:500px;font-size:15px;line-height:21px;color:var(--ink)}
.about-text p+p{margin-top:20px}
.about-visual{position:absolute;left:670px;top:585px;width:440px;height:345px;border-radius:12px;background:linear-gradient(160deg,#3a5fc4 0%,#8fa6d8 40%,#e6eaef 75%,#f4f5f7 100%)}
/* services */
.services-photo{position:absolute;left:148px;top:1164px;width:577px;height:360px;border:2px solid #c9d3da;border-radius:8px;background:linear-gradient(90deg,#2b2a28 0%,#45423d 49%,#7c7d7f 51%,#b9b6b0 75%,#5d5a55 100%)}
.service-list{position:absolute;left:778px;top:1193px;list-style:none;font-size:20px;color:var(--white);letter-spacing:.4px}
.service-list li{height:38.4px;display:flex;align-items:center;gap:14px}
.service-list .num{width:24px;height:24px;border-radius:50%;background:var(--sky);color:var(--navy);font-size:13px;display:flex;align-items:center;justify-content:center}
.service-list .hot{color:var(--red);padding-left:40px}
.service-list .hot .num{background:var(--red);color:var(--white)}
.btn-sky{position:absolute;background:var(--sky);color:var(--navy);font-family:"Roboto",sans-serif;font-weight:500;font-size:15px;display:flex;align-items:center;justify-content:center}
/* testimonials */
.card{position:absolute;top:1848px;width:496px;height:233px;background:var(--white);box-shadow:0 2px 10px rgba(0,0,0,.12)}
.avatar{position:absolute;left:22px;top:-28px;width:64px;height:64px;border-radius:50%;border:3px solid var(--sky);background:radial-gradient(circle at 50% 40%,#d9b79e,#7a5c4a)}
.quote{position:absolute;right:16px;top:2px;font-family:"Fira Sans",sans-serif;font-weight:700;font-size:72px;line-height:1;color:var(--red)}
.meta{position:absolute;left:24px;top:62px;display:flex;align-items:center;gap:12px;font-size:12px;font-weight:500}
.stars{color:#f5b800;font-size:15px;letter-spacing:3px}
.card-text{position:absolute;left:24px;top:86px;width:455px;font-size:14.5px;line-height:21px;color:var(--muted)}
.card-name{position:absolute;left:26px;top:165px;font-size:13px;color:var(--sky-deep)}
.card-role{position:absolute;left:26px;top:182px;font-size:11.5px;color:var(--ink)}
.arrow{position:absolute;width:30px;height:30px}
/* partners */
.partner{position:absolute;top:2387px;width:230px;height:108px;background:var(--white);border:1px solid #dcdcdc;display:flex;align-items:center;justify-content:center;gap:10px;font-family:"Fira Sans",sans-serif;font-weight:500;font-size:24px;color:#2a2a2a}
.partner i{width:16px;height:16px;border-radius:50%;background:#2a2a2a;display:block}
/* social feed */
.handle{position:absolute;left:375px;top:2656px;display:flex;align-items:center;gap:14px;font-family:"Roboto",sans-serif;font-weight:700;font-size:20px;color:var(--red)}
.handle i{width:40px;height:40px;border-radius:50%;border:4px solid var(--red);display:block}
.btn-follow{position:absolute;left:713px;top:2656px;width:111px;height:38px;border:2px solid var(--red);border-radius:3px;color:var(--red);font-family:"Roboto",sans-serif;font-size:15px;display:flex;align-items:center;justify-content:center}
.post{position:absolute;top:2730px;width:242px;height:241px;border:1px solid #e1e1e1}
.post-a{background:linear-gradient(180deg,#6c6a66,#3e3b38 50%,#a13030 80%,#55524e)}
.post-b{background:linear-gradient(180deg,#7a7773,#4a4744 50%,#2f2d2b 70%,#6d6a66)}
.post-c{background:linear-gradient(180deg,#3b3b3b,#1f1f1f)}
.post-d{background:linear-gradient(180deg,#585653,#8a8782 50%,#4a4845 75%,#a29f99)}
/* footer */
.brand.foot{left:89px;top:3264px;font-size:22px}
.foot-h{position:absolute;top:3187px;font-family:"Roboto",sans-serif;font-weight:500;font-size:19px;color:var(--sky)}
.foot-item{position:absolute;left:368px;display:flex;gap:14px;font-size:14.5px;line-height:20px;color:var(--white)}
.foot-item svg{flex:none;margin-top:2px}
.quick{position:absolute;left:710px;top:3222px;list-style:none;font-size:14.5px;color:var(--white)}
.quick li{height:26.5px}
.quick .active{color:var(--red);text-decoration:underline}
.map{position:absolute;left:918px;top:3176px;width:192px;height:192px;border-radius:50%;background:radial-gradient(circle at 40% 45%,#f4f5f6,#dfe3e6);border:3px solid #fff}
.copy-bar{position:absolute;left:0;top:3428px;width:1200px;height:42px;background:var(--red);color:var(--white);font-size:13px}
.copy-bar span{position:absolute;left:89px;top:12px}
.socials{position:absolute;left:1005px;top:14px;display:flex;gap:19px}
.socials i{width:13px;height:13px;border-radius:50%;background:var(--white);display:block}
</style>
</head>
<body>

<svg class="shapes" width="1200" height="3470" viewBox="0 0 1200 3470" aria-hidden="true">
  <defs>
    <linearGradient id="heroTone" x1="0" x2="1" y1="0" y2="1">
      <stop offset="0" stop-color="#2a333a"/>
      <stop offset=".5" stop-color="#151c22"/>
      <stop offset="1" stop-color="#0d2230"/>
    </linearGradient>
    <linearGradient id="navyTone" x1="0" x2="0" y1="0" y2="1">
      <stop offset="0" stop-color="#0a2436"/>
      <stop offset="1" stop-color="#0e3049"/>
    </linearGradient>
  </defs>
  <path d="M0 460 Q620 629 1200 430 V395 H0 Z" fill="var(--sky)"/>
  <path d="M0 0 H1200 V395 Q620 586 0 400 Z" fill="url(#heroTone)" role="img" aria-label="Engine bay photograph, half cleaned with dry ice"/>
  <rect x="0" y="950" width="1200" height="810" fill="url(#navyTone)"/>
  <path d="M270 1000 Q600 975 930 1000 Q600 990 270 1000 Z" fill="var(--sky)"/>
  <path d="M0 1760 Q600 1605 1200 1760 V1770 H0 Z" fill="var(--white)"/>
  <path d="M270 1706 Q600 1676 930 1706 Q600 1692 270 1706 Z" fill="var(--sky)"/>
  <rect x="0" y="2175" width="1200" height="470" fill="var(--gray-band)"/>
  <path d="M270 2222 Q600 2198 930 2222 Q600 2212 270 2222 Z" fill="var(--sky)"/>
  <path d="M0 2645 Q600 2540 1200 2645 Z" fill="var(--white)"/>
  <path d="M270 2594 Q600 2564 930 2594 Q600 2580 270 2594 Z" fill="var(--sky)"/>
  <path d="M0 3160 Q600 2967 1200 3110 V3428 H0 Z" fill="var(--sky)"/>
  <path d="M0 3195 Q600 3019 1200 3159 V3428 H0 Z" fill="var(--footer)"/>
</svg>

<div class="brand top"><span class="brand-dot"></span>Brixa Motor Gleam</div>
<nav class="nav">
  <span class="active">Home</span><span>About Us</span><span>Services</span><span>Result</span><span>Contact Us</span>
</nav>
<div class="btn-book">Book Now</div>
<h1 class="hero-title">DRY ICE CLEANING</h1>
<p class="hero-sub">Professional and Qualified Staff Members</p>
<div class="dots"><span></span><span class="on"></span><span></span></div>

<h2 class="h2" style="left:89px;top:638px">About Us</h2>
<div class="about-text">
  <p>We use super dry, compressed air to propel precisely processed, uniform particles of dry ice to clean and/or remove dirt and contaminants form vehicles concentrating mainly on undercarriage, engine bay and wheels/wheel wells.</p>
  <p>This process prevents water/moisture getting into areas of the vehicle you don't want it.</p>
</div>
<div class="about-visual" role="img" aria-label="Scoop of dry ice pellets releasing cold vapour"></div>

<h2 class="h2" style="left:0;width:1200px;text-align:center;top:1083px;letter-spacing:1px">Automotive Cleaning Services</h2>
<div class="services-photo" role="img" aria-label="Suspension parts before and after dry ice cleaning"></div>
<ol class="service-list">
  <li><span class="num">1</span>General Clean Up</li>
  <li><span class="num">2</span>Interior Shampoo</li>
  <li><span class="num">3</span>Interior Shampoo &amp; Wax</li>
  <li class="hot"><span class="num">4</span>Premium Package</li>
  <li><span class="num">5</span>Wash &amp; Wax</li>
  <li><span class="num">6</span>Exterior Protection</li>
  <li><span class="num">7</span>Exterior Detail &amp; Polish</li>
  <li><span class="num">8</span>Add Ons</li>
</ol>
<div class="btn-sky" style="left:493px;top:1565px;width:214px;height:38px">Book An Appointment</div>

<h2 class="h2" style="left:0;width:1200px;text-align:center;top:1748px">Testimonials</h2>
<div class="card" style="left:88px">
  <div class="avatar" role="img" aria-label="Client portrait"></div>
  <div class="quote">&ldquo;</div>
  <div class="meta"><span class="stars">★★★★★</span>Mar 09</div>
  <p class="card-text">Lorem Ipsum is simply dummy text of the printing and typesetting industry. Lorem Ipsum has been the industry's standard dummy text ever since the 1500s...</p>
  <div class="card-name">Marla V.</div>
  <div class="card-role">CEO, Harbor Crest Group</div>
</div>
<div class="card" style="left:616px">
  <div class="avatar" role="img" aria-label="Client portrait"></div>
  <div class="quote">&ldquo;</div>
  <div class="meta"><span class="stars">★★★★★</span>Mar 09</div>
  <p class="card-text">Lorem Ipsum is simply dummy text of the printing and typesetting industry. Lorem Ipsum has been the industry's standard dummy text ever since the 1500s...</p>
  <div class="card-name">Marla V.</div>
  <div class="card-role">CEO, Harbor Crest Group</div>
</div>
<svg class="arrow" style="left:42px;top:1950px" viewBox="0 0 30 30" aria-hidden="true"><circle cx="15" cy="15" r="13" fill="none" stroke="#9a9a9a" stroke-width="1.6"/><path d="M21 15H9M14 10l-5 5 5 5" fill="none" stroke="#9a9a9a" stroke-width="1.6"/></svg>
<svg class="arrow" style="left:1126px;top:1950px" viewBox="0 0 30 30" aria-hidden="true"><circle cx="15" cy="15" r="13" fill="none" stroke="var(--red)" stroke-width="1.6"/><path d="M9 15h12M16 10l5 5-5 5" fill="none" stroke="var(--red)" stroke-width="1.6"/></svg>
<div class="btn-sky" style="left:546px;top:2123px;width:109px;height:34px">View All</div>

<h2 class="h2" style="left:0;width:1200px;text-align:center;top:2305px">Businesses Associates</h2>
<div class="partner" style="left:101px"><i></i>Nordhav</div>
<div class="partner" style="left:357px">Staller-Kraus</div>
<div class="partner" style="left:613px">Corsaro</div>
<div class="partner" style="left:869px">Ashcombe</div>
<svg class="arrow" style="left:54px;top:2426px" viewBox="0 0 30 30" aria-hidden="true"><circle cx="15" cy="15" r="13" fill="none" stroke="#9a9a9a" stroke-width="1.6"/><path d="M21 15H9M14 10l-5 5 5 5" fill="none" stroke="#9a9a9a" stroke-width="1.6"/></svg>
<svg class="arrow" style="left:1116px;top:2426px" viewBox="0 0 30 30" aria-hidden="true"><circle cx="15" cy="15" r="13" fill="none" stroke="var(--red)" stroke-width="1.6"/><path d="M9 15h12M16 10l5 5-5 5" fill="none" stroke="var(--red)" stroke-width="1.6"/></svg>

<div class="handle"><i></i>@BRIXA-MOTOR-GLEAM-LLC</div>
<div class="btn-follow">Follow</div>
<div class="post post-a" style="left:89px" role="img" aria-label="Recent post: coil-over suspension before and after cleaning"></div>
<div class="post post-b" style="left:349px" role="img" aria-label="Recent post: control arms after dry ice treatment"></div>
<div class="post post-c" style="left:609px" role="img" aria-label="Recent post: red brake caliper detail"></div>
<div class="post post-d" style="left:869px" role="img" aria-label="Recent post: wheel hub and wheel well cleaned"></div>

<div class="brand foot"><span class="brand-dot"></span>Brixa Motor Gleam</div>
<div class="foot-h" style="left:368px">Conatct Info</div>
<div class="foot-item" style="top:3222px">
  <svg width="14" height="18" viewBox="0 0 14 18" aria-hidden="true"><path d="M7 1a6 6 0 0 0-6 6c0 4.5 6 10 6 10s6-5.5 6-10a6 6 0 0 0-6-6z" fill="none" stroke="var(--sky)" stroke-width="2"/><circle cx="7" cy="7" r="2" fill="var(--sky)"/></svg>
  <span>lorem ipsum, 88 Quarry Lane<br>Harlow Bay, HB &nbsp;2K4</span>
</div>
<div class="foot-item" style="top:3285px">
  <svg width="14" height="16" viewBox="0 0 14 16" aria-hidden="true"><path d="M3 1l3 3-2 2c1 2 3 4 5 5l2-2 3 3-2 3C6 15 0 9 1 3z" fill="var(--sky)"/></svg>
  <span>(555) 318-2047</span>
</div>
<div class="foot-item" style="top:3327px">
  <svg width="15" height="16" viewBox="0 0 15 16" aria-hidden="true"><rect x="1" y="4" width="13" height="9" fill="none" stroke="var(--sky)" stroke-width="1.8"/><path d="M1 4l6.5 5L14 4" fill="none" stroke="var(--sky)" stroke-width="1.8"/></svg>
  <span>info@brixamotorgleam.com</span>
</div>
<div class="foot-h" style="left:710px">Quick Link</div>
<ul class="quick">
  <li class="active">Home</li><li>About Us</li><li>Services</li><li>Result</li><li>Contact Us</li>
</ul>
<div class="map" role="img" aria-label="Street map showing the shop location"></div>
<div class="copy-bar">
  <span>Copyright © 2022 Brixa Motor Gleam llc. All Rights Reserved</span>
  <div class="socials"><i></i><i></i><i></i><i></i></div>
</div>

</body>
</html>
```